Brivo Packworks Website using Wix Platform

Project Overview:
Brivo Packworks is a supply chain company specializing in packaging and manufacturing services for CPG (Consumer Packaged Goods) brands and nutritional/dietary supplement companies. The company offers end-to-end solutions including packaging design, production, co-packing, and private labeling. The goal of this project is to create a professional, user-friendly website that showcases your expertise, builds trust with potential clients, and generates leads for your services.

Objectives:
Establish Brand Authority: Position Brivo Packworks as a leader in the packaging and manufacturing industry for CPG and nutritional products.
Lead Generation: Encourage visitors to contact you for quotes, consultations, or further information.
Professional User Experience: Ensure the website is easy to navigate, visually appealing, and mobile-friendly.
SEO & Conversion Optimization: Optimize the site for search engines to attract organic traffic and improve conversion rates.
Primary Audience:
CPG Brands: Companies in industries like food and beverage, personal care, and household products looking for packaging and manufacturing services.
Nutritional/Dietary Supplement Brands: Companies in the health and wellness industry needing specialized packaging and manufacturing services for supplements, including compliance with regulatory standards (GMP).
Secondary Audience:
Potential partners looking to collaborate on co-packing or private labeling.
Key Features & Functionality:
Responsive Design:

The website must be fully responsive, ensuring optimal viewing across all devices (desktops, tablets, mobile).
User-Centric Navigation:

A clean, intuitive navigation system that allows users to quickly access key pages such as Home, Services, About Us, Case Studies, FAQ, and Contact.
Lead Generation Forms:

Prominent CTAs (Calls to Action) throughout the website encouraging users to “Request a Quote”, “Get in Touch”, or “Learn More” about your services.
Contact Form: Simple form allowing potential clients to submit inquiries about your services.
SEO Optimization:

The site should be optimized for relevant keywords (e.g., “co-packing services for CPG,” “nutritional supplement packaging,” “custom packaging solutions”), including meta descriptions, headers, and on-page content.
Content Management System (CMS):

An easy-to-use CMS (like WordPress or Webflow) for easy content updates. This will allow you to make changes to your services, case studies, and other sections without requiring a developer.
Analytics Integration:

Google Analytics or a similar tool for tracking site visitors and performance metrics to make data-driven decisions on site improvements.
Site Structure & Content:
1. Home Page:
Hero Section with tagline, images or video of your services in action, and a clear CTA (e.g., “Request a Quote”).
Value Proposition: Short and compelling introduction to Brivo Packworks’s core services and advantages.
Overview of Services: Highlight your key offerings (e.g., Packaging Design, Co-packing, Nutritional Supplement Packaging, Private Labeling).
Client Logos/Testimonials: Social proof to establish credibility.
CTA Buttons: Throughout the page to drive conversions (e.g., “Get a Free Consultation”).
2. About Us Page:
Company Overview: Explain your mission, values, and commitment to quality.
Team Overview (Optional): Introduce key team members to humanize your company and build trust.
Core Values and Differentiators: Showcase what makes Brivo Packworks unique—sustainability practices, regulatory compliance, and industry expertise.
3. Services Pages (Separate Pages for Each Service):
Packaging & Design: Custom packaging solutions, materials, and design services for CPG brands.
Manufacturing & Assembly: Your end-to-end production process, assembly capabilities, and how you support both small and large-scale runs.
Nutritional & Dietary Supplement Packaging: Focus on specialized packaging for supplements, regulatory compliance (GMP), and certifications.
Private Labeling: Services for clients who wish to brand their own products using your packaging.
Each service page will include detailed descriptions, benefits, process information, and CTAs like “Get Started” or “Request a Quote”.
4. Case Studies / Portfolio Page:
Success Stories: Showcase in-depth case studies of past projects, especially successful partnerships with CPG or supplement brands.
Before & After Images: Display the difference your services have made for clients, especially in terms of packaging quality or branding improvements.
Client Testimonials: Additional customer feedback to strengthen your brand reputation.
5. FAQ Page:
Address common questions related to lead times, regulatory compliance, order quantities, and specific details for different industries (e.g., dietary supplements).
The format will be accordion-style or dropdowns for easy scanning.
6. Contact Us Page:
Contact Form: With fields for name, email, company, and inquiry details.
Location Information: Physical address, phone number, and working hours.
Map Integration: If relevant, integrate Google Maps to show your office location.
Social Media Links: Link to your company’s LinkedIn, Instagram, or other relevant platforms.

Target Market(s)

Startup CPG Brands, Supplement Brands, Nutrition Brands

Industry/Entity Type

Flexible Packaging, Contract Manufacturing, Supplement & Food Manufacturing

Coding

Coded - Design and coding required

Number of Pages Required

5+ page

Requirements
Must have
• Use our colors.
Nice to have
• https://tornap482.sitebuildhost.example/brivopackworks - www.ninefoldlane.example - www.pelkasnacks.example - thebrightmill.example

```html
<!DOCTYPE html>
<html lang="en">
<head>
<meta charset="utf-8">
<title>Brivo Packworks — Packaging &amp; Manufacturing Services</title>
<link href="https://fonts.googleapis.com/css2?family=Arimo:wght@400;500&family=Poppins:wght@400;500;600&display=swap" rel="stylesheet">
<style>
:root{
  --navy:#262944;
  --navy-deep:#1f2139;
  --green:#7fdd3d;
  --ink:#2a2a33;
  --muted:#5a5a66;
  --line:#e4e4ea;
  --field:#ffffff;
  --white:#ffffff;
}
*{margin:0;padding:0;box-sizing:border-box}
html,body{width:1200px;height:4934px;overflow:hidden}
body{position:relative;background:var(--white);font-family:"Poppins",sans-serif;color:var(--ink)}
.abs{position:absolute}
h1,h2,h3{font-weight:400}
.heading{font-family:"Arimo",sans-serif;font-weight:400;color:var(--navy);letter-spacing:.5px}
.brand{font-family:"Poppins",sans-serif;font-weight:400;font-size:19px;color:var(--white);letter-spacing:.5px;display:flex;align-items:center;gap:10px}
.brand-box{width:18px;height:18px;border:2px solid var(--white)}

/* top bar */
.topbar{left:0;top:0;width:1200px;height:92px;background:var(--navy)}
.top-contact{display:flex;align-items:center;gap:14px;font-size:13px;color:var(--white);line-height:1.35}
.top-contact b{display:block;color:var(--green);font-weight:500}
/* nav */
.nav{left:0;top:92px;width:1200px;height:71px;background:var(--white);box-shadow:0 2px 6px rgba(0,0,0,.05)}
.nav a{position:absolute;top:25px;font-size:15px;font-weight:500;color:var(--ink);text-decoration:none;letter-spacing:.3px}
.nav a.active{color:var(--green);border-bottom:2px solid var(--green);padding-bottom:3px}

/* hero */
.hero{left:0;top:163px;width:1200px;height:720px;background:linear-gradient(100deg,#2a2d4a 0%,#2f3356 40%,#5b5f80 60%,#a28a6c 85%,#c7ad8c 100%)}
.hero-shade{left:0;top:163px;width:1200px;height:720px;background:linear-gradient(90deg,rgba(30,32,56,.85) 0%,rgba(30,32,56,.55) 45%,rgba(30,32,56,0) 75%)}
.hero-title{left:67px;top:318px;font-family:"Arimo",sans-serif;font-size:66px;color:var(--white);font-weight:400}
.hero-sub{left:72px;top:405px;font-size:35px;line-height:49px;color:var(--white);font-weight:400}
.btn{position:absolute;display:flex;align-items:center;justify-content:center;font-size:16px;font-weight:600;letter-spacing:.3px;border-radius:0 22px 0 22px;text-decoration:none}
.btn-dark{background:var(--navy);color:var(--white);box-shadow:-5px -5px 0 var(--green)}
.btn-light{background:var(--white);color:var(--navy);box-shadow:-5px -5px 0 var(--green)}
.btn-green{background:var(--green);color:var(--navy);box-shadow:-5px -5px 0 var(--white)}
.scroll-btn{left:582px;top:760px;width:38px;height:52px;border-radius:20px;background:var(--white);border:2px solid #d0d0d8;display:flex;align-items:center;justify-content:center}

/* about */
.title-lg{font-size:50px}
.eyebrow{font-size:16px;font-weight:500;color:var(--navy);display:flex;align-items:center;gap:14px;letter-spacing:.3px}
.eyebrow i{display:block;width:82px;height:3px;background:var(--green)}
.eyebrow.center{justify-content:center}
.body-text{font-size:13.6px;line-height:26.5px;color:var(--muted)}
.frame{border:6px solid var(--green)}

/* services */
.card{background:var(--white);box-shadow:0 3px 12px rgba(0,0,0,.12)}
.card-img{position:absolute;left:0;top:0;width:100%;height:226px}
.card-corner{position:absolute;right:0;top:0}
.card h3{position:absolute;left:0;width:100%;top:258px;text-align:center;font-family:"Arimo",sans-serif;font-weight:500;font-size:22px;color:var(--ink);letter-spacing:.5px}
.card p{position:absolute;left:40px;right:40px;top:298px;text-align:center;font-size:13.6px;line-height:25px;color:var(--muted)}
.read-more{position:absolute;left:0;width:100%;top:396px;display:flex;justify-content:center;align-items:center;gap:10px;font-size:13px;font-weight:600;color:var(--navy)}
.read-more span{text-decoration:underline}

/* cta band */
.cta-title{left:0;width:1200px;top:2990px;text-align:center;font-family:"Arimo",sans-serif;font-weight:400;font-size:56px;line-height:63px;color:var(--white)}

/* testimonials */
.quote-card{width:520px;height:170px}
.avatar{position:absolute;left:0;top:0;width:92px;height:92px;border-radius:50%;background:radial-gradient(circle at 50% 40%,#d9d4cf,#8f8a86)}
.quote-text{position:absolute;left:114px;top:0;width:322px;font-size:13.6px;line-height:23px;color:var(--muted);text-align:justify}
.quote-mark{color:var(--green);font-family:"Arimo",sans-serif;font-size:34px;font-weight:700;line-height:0;position:relative;top:14px;margin-right:8px}
.quote-name{position:absolute;left:114px;top:104px;font-size:18px;font-weight:500;color:var(--ink)}
.stars{position:absolute;left:114px;top:132px;display:flex;gap:2px}
.arrow-btn{width:40px;height:40px;border-radius:50%;display:flex;align-items:center;justify-content:center}

/* contact */
.field{position:absolute;background:var(--field);border:1px solid var(--line);box-shadow:0 2px 6px rgba(0,0,0,.06);font-size:12px;color:#9a9aa5;padding:10px 18px}

/* footer */
.footer-contact{display:flex;align-items:center;gap:18px;font-size:13px;color:var(--white);line-height:18px}
.icon-box{width:22px;height:22px;border-radius:5px;background:var(--green);display:flex;align-items:center;justify-content:center}
.footer-links a{position:absolute;top:4826px;font-size:14.5px;color:var(--white);text-decoration:none}
.social{width:26px;height:26px;border:1.5px solid var(--white)}
</style>
</head>
<body>

<header class="abs topbar">
  <div class="abs brand" style="left:69px;top:31px"><span class="brand-box"></span>BRIVO PACKWORKS</div>
  <div class="abs top-contact" style="left:728px;top:28px">
    <svg width="24" height="24" viewBox="0 0 24 24"><path d="M6 3l3 4-2 2c1 3 4 6 7 7l2-2 4 3-2 4C10 21 3 14 3 5z" fill="none" stroke="var(--green)" stroke-width="1.8"/></svg>
    <div><b>Call:</b>012-555-0147</div>
  </div>
  <div class="abs top-contact" style="left:912px;top:28px">
    <svg width="24" height="20" viewBox="0 0 24 20"><rect x="1" y="2" width="22" height="16" fill="var(--green)"/><path d="M1 2l11 9 11-9" fill="none" stroke="var(--navy)" stroke-width="1.6"/></svg>
    <div><b>Email:</b>hello@brivopack.example</div>
  </div>
</header>

<nav class="abs nav">
  <a class="active" style="left:176px">HOME</a>
  <a style="left:302px">SERVICES</a>
  <a style="left:460px">ABOUT US</a>
  <a style="left:617px">CASE STUDIES</a>
  <a style="left:809px">FAQ</a>
  <a style="left:920px">CONTACT US</a>
</nav>

<section>
  <div class="abs hero" role="img" aria-label="Worker sealing a cardboard box with a tape dispenser"></div>
  <div class="abs hero-shade"></div>
  <h1 class="abs hero-title">BRIVO PACKWORKS</h1>
  <p class="abs hero-sub">We specialized in packaging and<br>manufacturing services</p>
  <a class="btn btn-dark" style="left:72px;top:568px;width:216px;height:64px">REQUEST A QUOTE</a>
  <a class="btn btn-light" style="left:314px;top:568px;width:292px;height:64px">GET A FREE CONSULTATION</a>
  <svg class="abs" style="left:0;top:760px" width="1200" height="130" viewBox="0 0 1200 130">
    <polygon points="0,110 600,22 1200,110 1200,130 0,130" fill="var(--white)"/>
    <polyline points="0,112 600,24 1200,112" fill="none" stroke="var(--green)" stroke-width="7"/>
  </svg>
  <div class="abs scroll-btn"><svg width="12" height="18" viewBox="0 0 12 18"><path d="M6 1v15M1 11l5 5 5-5" fill="none" stroke="var(--navy)" stroke-width="1.6"/></svg></div>
</section>

<section>
  <h2 class="abs heading title-lg" style="left:98px;top:995px">ABOUT US</h2>
  <div class="abs eyebrow" style="left:98px;top:1048px">WHO WE ARE<i></i></div>
  <p class="abs body-text" style="left:98px;top:1098px;width:428px;text-align:justify">Lorem ipsum dolor sit amet, consectetur adipiscing elit. Sed pharetra, turpis vitae tincidunt tempus, ipsum magna varius mauris, et dictum nulla neque ac turpis. Etiam finibus est metus, eu viverra velit auctor ac. Nam luctus lorem felis, quis vulputate quam convallis elementum. Maecenas malesuada risus vitae tristique imperdiet. Interdum et malesuada fames ac ante ipsum primis in faucibus. Cras tristique nunc a tellus semper, et ultrices mauris vulputate.</p>
  <a class="btn btn-dark" style="left:103px;top:1347px;width:227px;height:52px;font-size:12.5px">LEARN MORE ABOUT US</a>

  <div class="abs frame" style="left:601px;top:947px;width:410px;height:300px;border-bottom:none"></div>
  <div class="abs" role="img" aria-label="Warehouse worker taping a parcel box" style="left:596px;top:953px;width:408px;height:483px;background:linear-gradient(160deg,#b89e84 0%,#4d5a3c 40%,#a48560 75%,#c49a6a 100%)"></div>
  <div class="abs" style="left:788px;top:1211px;width:320px;height:277px;background:var(--white)"></div>
  <div class="abs" role="img" aria-label="Packer in a safety vest preparing shipping boxes" style="left:794px;top:1217px;width:308px;height:265px;background:linear-gradient(135deg,#8a6a4e 0%,#d9a07a 35%,#e4e0da 60%,#b08a64 100%)"></div>
</section>

<section>
  <h2 class="abs heading title-lg" style="left:0;width:1200px;top:1570px;text-align:center">OUR SERVICES</h2>
  <div class="abs eyebrow center" style="left:0;width:1200px;top:1625px"><i style="width:64px"></i>WHAT WE DO<i style="width:64px"></i></div>
  <p class="abs body-text" style="left:100px;width:1000px;top:1688px;text-align:center;font-size:13.6px">Lorem ipsum dolor sit amet, consectetur adipiscing elit. Sed pharetra, turpis vitae tincidunt tempus, ipsum magna varius mauris,<br>et dictum nulla neque ac turpis. Etiam finibus est metus, eu viverra velit auctor ac.</p>

  <article class="abs card" style="left:67px;top:1804px;width:520px;height:447px">
    <div class="card-img" role="img" aria-label="Juice bottles and kraft product boxes on a table" style="background:linear-gradient(100deg,#8a3a2e 0%,#d58a3c 30%,#cdbba4 60%,#b98a62 100%)"></div>
    <svg class="card-corner" width="36" height="54"><polygon points="0,0 36,0 36,54" fill="var(--green)"/></svg>
    <h3>PACKAGING DESIGN</h3>
    <p>Lorem ipsum dolor sit amet, consectetur adipiscing elit. Morbi vitae velit ac velit vulputate placerat commodo at mauris. Donec facilisis semper leo eu vulputate.</p>
    <div class="read-more"><span>READ MORE</span><svg width="18" height="10"><path d="M0 5h16M12 1l4 4-4 4" fill="none" stroke="var(--green)" stroke-width="1.8"/></svg></div>
  </article>
  <article class="abs card" style="left:613px;top:1804px;width:522px;height:447px">
    <div class="card-img" role="img" aria-label="Hands taping a box with a dispenser" style="background:linear-gradient(100deg,#3a3d44 0%,#c9c3bc 35%,#b99a78 65%,#5a5e46 100%)"></div>
    <svg class="card-corner" width="36" height="54"><polygon points="0,0 36,0 36,54" fill="var(--green)"/></svg>
    <h3>CO-PACKING</h3>
    <p>Lorem ipsum dolor sit amet, consectetur adipiscing elit. Morbi vitae velit ac velit vulputate placerat commodo at mauris. Donec facilisis semper leo eu vulputate.</p>
    <div class="read-more"><span>READ MORE</span><svg width="18" height="10"><path d="M0 5h16M12 1l4 4-4 4" fill="none" stroke="var(--green)" stroke-width="1.8"/></svg></div>
  </article>
  <article class="abs card" style="left:67px;top:2279px;width:520px;height:445px">
    <div class="card-img" role="img" aria-label="Stacked blank supplement pouches" style="background:linear-gradient(100deg,#c9c0b2 0%,#9a8c7a 35%,#b8a48a 55%,#e3dfd8 100%)"></div>
    <svg class="card-corner" width="36" height="54"><polygon points="0,0 36,0 36,54" fill="var(--green)"/></svg>
    <h3>NUTRITIONAL SUPPLEMENT PACKAGING</h3>
    <p>Lorem ipsum dolor sit amet, consectetur adipiscing elit. Morbi vitae velit ac velit vulputate placerat commodo at mauris. Donec facilisis semper leo eu vulputate.</p>
    <div class="read-more"><span>READ MORE</span><svg width="18" height="10"><path d="M0 5h16M12 1l4 4-4 4" fill="none" stroke="var(--green)" stroke-width="1.8"/></svg></div>
  </article>
  <article class="abs card" style="left:613px;top:2279px;width:522px;height:445px">
    <div class="card-img" role="img" aria-label="Person labeling a parcel with a tape gun" style="background:linear-gradient(100deg,#d8d4d2 0%,#6a6e8a 35%,#e06a3a 60%,#c7a07a 100%)"></div>
    <svg class="card-corner" width="36" height="54"><polygon points="0,0 36,0 36,54" fill="var(--green)"/></svg>
    <h3>PRIVATE LABELING</h3>
    <p>Lorem ipsum dolor sit amet, consectetur adipiscing elit. Morbi vitae velit ac velit vulputate placerat commodo at mauris. Donec facilisis semper leo eu vulputate.</p>
    <div class="read-more"><span>READ MORE</span><svg width="18" height="10"><path d="M0 5h16M12 1l4 4-4 4" fill="none" stroke="var(--green)" stroke-width="1.8"/></svg></div>
  </article>
</section>

<section>
  <svg class="abs" style="left:0;top:2860px" width="1200" height="620" viewBox="0 0 1200 620" role="img" aria-label="Dark overlay on a packing workshop scene">
    <defs><linearGradient id="ctaFill" x1="0" x2="1" y1="0" y2="0"><stop offset="0" stop-color="#2a2d48"/><stop offset=".5" stop-color="#262944"/><stop offset="1" stop-color="#23263f"/></linearGradient></defs>
    <polygon points="0,110 600,0 1200,110 1200,614 0,614" fill="url(#ctaFill)"/>
  </svg>
  <h2 class="abs cta-title">PACKAGING AND<br>MANUFACTURING SERVICES<br>ARE AVAILABLE HERE</h2>
  <div class="abs" style="left:487px;top:3203px;width:226px;height:4px;background:var(--green)"></div>
  <a class="btn btn-green" style="left:450px;top:3264px;width:305px;height:66px;font-size:16px">GET A FREE CONSULTATION</a>
</section>

<section>
  <h2 class="abs heading title-lg" style="left:0;width:1200px;top:3538px;text-align:center">CLIENT TESTIMONIALS</h2>
  <div class="abs eyebrow center" style="left:0;width:1200px;top:3595px"><i style="width:64px"></i>CLIENT REVIEWS<i style="width:64px"></i></div>

  <div class="abs arrow-btn" style="left:53px;top:3712px;background:#b9b9c2"><svg width="10" height="14"><path d="M8 1L2 7l6 6" fill="none" stroke="var(--white)" stroke-width="1.8"/></svg></div>
  <div class="abs arrow-btn" style="left:1111px;top:3712px;background:var(--navy)"><svg width="10" height="14"><path d="M2 1l6 6-6 6" fill="none" stroke="var(--white)" stroke-width="1.8"/></svg></div>

  <div class="abs quote-card" style="left:144px;top:3675px">
    <div class="avatar" role="img" aria-label="Client portrait"></div>
    <p class="quote-text"><span class="quote-mark">“</span>Lorem ipsum dolor sit amet, con sectetur adipiscing elit. Maece nas ac tellus ac ipsum porta viverra sit amet sed leo. Vivamus eu mauris convallis, hendrerit</p>
    <div class="quote-name">Marlow Teague</div>
    <div class="stars"><svg width="70" height="13" viewBox="0 0 70 13"><g fill="var(--green)"><polygon points="6.5,0 8.3,4.5 13,4.8 9.4,7.9 10.5,12.5 6.5,10 2.5,12.5 3.6,7.9 0,4.8 4.7,4.5"/><polygon transform="translate(14)" points="6.5,0 8.3,4.5 13,4.8 9.4,7.9 10.5,12.5 6.5,10 2.5,12.5 3.6,7.9 0,4.8 4.7,4.5"/><polygon transform="translate(28)" points="6.5,0 8.3,4.5 13,4.8 9.4,7.9 10.5,12.5 6.5,10 2.5,12.5 3.6,7.9 0,4.8 4.7,4.5"/><polygon transform="translate(42)" points="6.5,0 8.3,4.5 13,4.8 9.4,7.9 10.5,12.5 6.5,10 2.5,12.5 3.6,7.9 0,4.8 4.7,4.5"/><polygon transform="translate(56)" points="6.5,0 8.3,4.5 13,4.8 9.4,7.9 10.5,12.5 6.5,10 2.5,12.5 3.6,7.9 0,4.8 4.7,4.5"/></g></svg></div>
  </div>
  <div class="abs quote-card" style="left:623px;top:3675px">
    <div class="avatar" role="img" aria-label="Client portrait"></div>
    <p class="quote-text"><span class="quote-mark">“</span>Lorem ipsum dolor sit amet, con sectetur adipiscing elit. Maece nas ac tellus ac ipsum porta viverra sit amet sed leo. Vivamus eu mauris convallis, hendrerit</p>
    <div class="quote-name">Orla Penwright</div>
    <div class="stars"><svg width="70" height="13" viewBox="0 0 70 13"><g fill="var(--green)"><polygon points="6.5,0 8.3,4.5 13,4.8 9.4,7.9 10.5,12.5 6.5,10 2.5,12.5 3.6,7.9 0,4.8 4.7,4.5"/><polygon transform="translate(14)" points="6.5,0 8.3,4.5 13,4.8 9.4,7.9 10.5,12.5 6.5,10 2.5,12.5 3.6,7.9 0,4.8 4.7,4.5"/><polygon transform="translate(28)" points="6.5,0 8.3,4.5 13,4.8 9.4,7.9 10.5,12.5 6.5,10 2.5,12.5 3.6,7.9 0,4.8 4.7,4.5"/><polygon transform="translate(42)" points="6.5,0 8.3,4.5 13,4.8 9.4,7.9 10.5,12.5 6.5,10 2.5,12.5 3.6,7.9 0,4.8 4.7,4.5"/><polygon transform="translate(56)" points="6.5,0 8.3,4.5 13,4.8 9.4,7.9 10.5,12.5 6.5,10 2.5,12.5 3.6,7.9 0,4.8 4.7,4.5"/></g></svg></div>
  </div>
</section>

<section>
  <div class="abs" style="left:65px;top:3953px;width:418px;height:460px;border-left:6px solid var(--green);border-top:6px solid var(--green)"></div>
  <div class="abs" role="img" aria-label="Hands sealing a box with a blue tape dispenser" style="left:73px;top:3961px;width:406px;height:448px;background:linear-gradient(115deg,#c2aa8c 0%,#9c8062 30%,#2e3a7a 55%,#1f2a5e 75%,#c9b8a4 100%)"></div>
  <svg class="abs" style="left:419px;top:3961px" width="60" height="80"><polygon points="0,0 60,0 60,80" fill="var(--green)"/></svg>

  <h2 class="abs heading title-lg" style="left:546px;top:3942px">CONTACT US</h2>
  <div class="abs eyebrow" style="left:548px;top:3995px">GET IN TOUCH WITH<i style="width:70px"></i></div>
  <p class="abs" style="left:550px;top:4046px;width:575px;font-size:13px;line-height:24px;color:var(--muted)">If you have any questions or need help, please fill out the form below. We are here to help and answer any questions you might have. We look forward to hearing from you.</p>
  <div class="field" style="left:546px;top:4139px;width:552px;height:37px">Name:</div>
  <div class="field" style="left:546px;top:4186px;width:269px;height:37px">Phone:</div>
  <div class="field" style="left:828px;top:4186px;width:270px;height:37px">Email:</div>
  <div class="field" style="left:546px;top:4233px;width:552px;height:74px">Message:</div>
  <a class="btn btn-dark" style="left:554px;top:4350px;width:178px;height:52px;font-size:13.5px">SUBMIT NOW</a>
</section>

<footer>
  <svg class="abs" style="left:0;top:4524px" width="1200" height="410" viewBox="0 0 1200 410">
    <polygon points="0,106 600,0 1200,106 1200,410 0,410" fill="var(--navy)"/>
  </svg>
  <div class="abs brand" style="left:0;width:1200px;top:4632px;justify-content:center;font-size:21px"><span class="brand-box"></span>BRIVO PACKWORKS</div>

  <div class="abs footer-contact" style="left:236px;top:4716px">
    <div class="icon-box"><svg width="12" height="12" viewBox="0 0 24 24"><path d="M6 3l3 4-2 2c1 3 4 6 7 7l2-2 4 3-2 4C10 21 3 14 3 5z" fill="var(--white)"/></svg></div>
    <div>CALL US<br>8012 555 0147</div>
  </div>
  <div class="abs footer-contact" style="left:430px;top:4716px">
    <div class="icon-box"><svg width="12" height="10"><rect x=".5" y=".5" width="11" height="9" fill="none" stroke="var(--white)"/><path d="M1 1l5 4 5-4" fill="none" stroke="var(--white)"/></svg></div>
    <div>EMAIL US<br>hello@brivopack.example</div>
  </div>
  <div class="abs footer-contact" style="left:687px;top:4716px">
    <div class="icon-box"><svg width="10" height="13" viewBox="0 0 10 13"><path d="M5 13C2 9 0 7 0 5a5 5 0 0110 0c0 2-2 4-5 8z" fill="var(--white)"/><circle cx="5" cy="5" r="1.8" fill="var(--green)"/></svg></div>
    <div>Address line Dummy Here<br>Address line Here</div>
  </div>

  <div class="abs" style="left:69px;top:4796px;width:1066px;height:1px;background:rgba(255,255,255,.25)"></div>
  <nav class="footer-links">
    <a style="left:210px">HOME</a>
    <a style="left:327px">SERVICES</a>
    <a style="left:471px">ABOUT US</a>
    <a style="left:616px">CASE STUDIES</a>
    <a style="left:792px">FAQ</a>
    <a style="left:896px">CONTACT US</a>
  </nav>
  <div class="abs" style="left:69px;top:4870px;width:1066px;height:1px;background:rgba(255,255,255,.25)"></div>
  <p class="abs" style="left:69px;top:4902px;font-size:11px;color:var(--white)">Copyright © 2024 All Rights Reserved By Company name</p>
  <div class="abs" style="left:1012px;top:4894px;display:flex;gap:5px">
    <span class="social"></span><span class="social"></span><span class="social"></span><span class="social"></span>
  </div>
</footer>

</body>
</html>
```